Business Card Design for Small Electrical Contractor

I need to update my business card into something a little more modern. We are a small electrical contracting company. We service domestic and commercial places around Sydney. We have 2 logo designs at the moment. I have uploaded both and 2 different sizes to work with.

Industry/Entity Type

Business

Contact Information for Business Card

Ted Corbin
8/21-23 Holt St, Fernhaven 2087
t - (02) 9471 3820
m - 0427 915 304
E - info@corbinelec.example.au
W - corbinelec.example.au
ABN: 42 907 518 263

Font styles to use
Sans Serif

Requirements
Must have
• I would also like to see the below fit on somewhere aswell
• - Licensed Electrician
• - Level 2 (Cat 1 & 4)
• - Domestic
• - Commercial
• - Repairs and Installations
• - Data
Nice to have
• Try and keep similar colours as logo
Should not have
• No lightning bolts or light globes. Smart and professional please.

```html
<!DOCTYPE html>
<html lang="en">
<head>
<meta charset="utf-8">
<title>T&amp;R Corbin Electrical – Business Card</title>
<link href="https://fonts.googleapis.com/css2?family=Raleway:wght@400;500;700;800&display=swap" rel="stylesheet">
<style>
  :root {
    --teal-deep: #0b3d38;
    --teal-black: #051614;
    --accent-orange: #f0a020;
    --card-white: #ffffff;
    --stage: #e6e7e6;
    --ink: #0b3d38;
  }
  * { margin: 0; padding: 0; box-sizing: border-box; }
  html, body {
    width: 1200px; height: 913px; overflow: hidden;
    background: var(--stage);
    font-family: "Raleway", sans-serif;
  }
  .sheet {
    position: relative; width: 1200px; height: 913px;
    display: flex; align-items: center; justify-content: center; gap: 40px;
  }
  .card {
    position: relative; width: 540px; height: 309px;
    background: var(--card-white);
    box-shadow: 0 6px 18px rgba(0,0,0,0.18);
    overflow: hidden;
  }
  .card svg.card-art { position: absolute; inset: 0; }

  /* Front */
  .brand {
    position: absolute; left: 0; right: 0; top: 78px;
    text-align: center;
    font-weight: 700; font-size: 30px; letter-spacing: 0.5px;
    color: var(--ink);
  }
  .brand-rule {
    position: absolute; left: 170px; top: 124px; width: 200px; height: 2px;
    background: var(--accent-orange);
  }
  .services {
    position: absolute; left: 0; right: 0; top: 190px;
    text-align: center; color: #fff;
    font-size: 14.5px; font-weight: 400; line-height: 1.45;
  }

  /* Back */
  .holder {
    position: absolute; left: 40px; top: 112px;
    color: #fff; font-size: 28px; font-weight: 400;
  }
  .holder strong { font-weight: 800; letter-spacing: 1px; }
  .contacts {
    position: absolute; left: 40px; top: 168px;
    list-style: none; color: #fff; font-size: 14px; font-weight: 400;
  }
  .contacts li { display: flex; align-items: center; gap: 10px; height: 24px; }
  .contacts li.abn { padding-left: 30px; }
  .contacts svg { width: 20px; height: 20px; flex: none; }
  .address {
    position: absolute; right: 20px; top: 30px; width: 180px;
    text-align: center; color: var(--ink); font-size: 14px; line-height: 1.35;
  }
  .address svg { display: block; margin: 0 auto 6px; width: 20px; height: 20px; }
</style>
</head>
<body>
<main class="sheet">

  <section class="card card-front" aria-label="Card front">
    <svg class="card-art" width="540" height="309" viewBox="0 0 540 309">
      <g stroke="var(--teal-deep)" stroke-width="2" fill="none">
        <line x1="0" y1="203" x2="540" y2="203"/>
        <line x1="0" y1="209" x2="540" y2="209"/>
        <line x1="0" y1="249" x2="540" y2="249"/>
        <line x1="0" y1="255" x2="540" y2="255"/>
      </g>
      <polygon points="78,178 462,178 476,192 476,264 462,278 78,278 64,264 64,192" fill="var(--card-white)" stroke="var(--teal-deep)" stroke-width="2"/>
      <polygon points="84,184 456,184 468,196 468,260 456,272 84,272 72,260 72,196" fill="var(--teal-deep)"/>
    </svg>
    <div class="brand">T&amp;R Corbin Electrical</div>
    <div class="brand-rule"></div>
    <p class="services">Licensed Electrician | Level 2 (Cat 1 &amp; 4) | Domestic<br>Commercial | Repairs and Installations | Data</p>
  </section>

  <section class="card card-back" aria-label="Card back">
    <svg class="card-art" width="540" height="309" viewBox="0 0 540 309">
      <defs>
        <linearGradient id="backShade" x1="0" y1="0" x2="0.3" y2="1">
          <stop offset="0" stop-color="var(--teal-deep)"/>
          <stop offset="1" stop-color="var(--teal-black)"/>
        </linearGradient>
      </defs>
      <polygon points="0,34 150,62 190,20 330,20 300,62 540,230 540,309 0,309" fill="url(#backShade)"/>
    </svg>

    <div class="address">
      <svg viewBox="0 0 20 20" aria-hidden="true"><circle cx="10" cy="10" r="10" fill="var(--teal-deep)"/><path d="M10 5 L15 9.5 H13.5 V14.5 H11 V11.5 H9 V14.5 H6.5 V9.5 H5 Z" fill="#fff"/></svg>
      8/21-23 Holt St<br>Fernhaven 2087
    </div>

    <h1 class="holder">Ted <strong>CORBIN</strong></h1>
    <ul class="contacts">
      <li><svg viewBox="0 0 20 20" aria-hidden="true"><circle cx="10" cy="10" r="10" fill="#fff"/><path d="M6.5 5.5 L8.5 5.2 L9.5 8 L8.3 9 Q9.3 11 11 11.8 L12 10.6 L14.8 11.6 L14.5 13.6 Q10 14.5 6.5 9.5 Z" fill="var(--teal-deep)"/></svg>(02) 9471 3820</li>
      <li><svg viewBox="0 0 20 20" aria-hidden="true"><circle cx="10" cy="10" r="10" fill="#fff"/><rect x="7" y="4.5" width="6" height="11" rx="1" fill="var(--teal-deep)"/><rect x="8" y="6" width="4" height="7" fill="#fff"/></svg>0427 915 304</li>
      <li><svg viewBox="0 0 20 20" aria-hidden="true"><circle cx="10" cy="10" r="10" fill="#fff"/><circle cx="10" cy="10" r="5.5" fill="none" stroke="var(--teal-deep)" stroke-width="1.4"/><ellipse cx="10" cy="10" rx="2.3" ry="5.5" fill="none" stroke="var(--teal-deep)" stroke-width="1.2"/><line x1="4.5" y1="10" x2="15.5" y2="10" stroke="var(--teal-deep)" stroke-width="1.2"/></svg>corbinelec.example.au</li>
      <li><svg viewBox="0 0 20 20" aria-hidden="true"><circle cx="10" cy="10" r="10" fill="#fff"/><rect x="5" y="6.5" width="10" height="7" fill="var(--teal-deep)"/><path d="M5 6.5 L10 10.5 L15 6.5" fill="none" stroke="#fff" stroke-width="1"/></svg>info@corbinelec.example.au</li>
      <li class="abn">ABN: 42 907 518 263</li>
    </ul>
  </section>

</main>
</body>
</html>
```